Kelmora Legal Business Card

I require a corporate business card for a new legal services business.

I do not have a logo, nor do I want one.

I require a clean, neat a professional card for a law firm.

Details:

Business Name: Kelmora Legal
Name: Debra Lindqvist
Title: Corporate Services Manager
Location: Office 14 (Top Floor), Toravel Business Centre, Quinlan Grove Street, Alotau CBD, Milne Bay Province.
Postal Address: PO Box 593, Alotau, 211, Milne Bay Province, Papua New Guinea.
Contact: T: +675 6418250, F: +675 6413362, M: +675 72915867, E: dlindqvist@kelmoraexample.com.pg.

I look forward to your design submissions.

Industry/Entity Type

Legal

```html
<!DOCTYPE html>
<html lang="en">
<head>
<meta charset="utf-8">
<title>Kelmora Legal – Business Card</title>
<link rel="stylesheet" href="https://fonts.googleapis.com/css2?family=Roboto+Condensed:wght@400&display=swap">
<style>
  :root {
    --backdrop: #ecebe9;
    --card: #ffffff;
    --plum: #7b2160;
    --ink: #1e1e1e;
    --on-plum: #ffffff;
  }
  * { box-sizing: border-box; margin: 0; padding: 0; }
  html, body {
    width: 1200px; height: 800px; overflow: hidden;
    background: var(--backdrop);
    font-family: "Roboto Condensed", "Arial Narrow", sans-serif;
    color: var(--ink);
  }
  .business-card {
    position: absolute; left: 120px; top: 145px;
    width: 960px; height: 510px;
    background: var(--card);
    box-shadow: 0 2px 10px rgba(0,0,0,0.18);
  }
  .accent-band {
    position: absolute; left: 0; top: 87px;
    width: 432px; height: 69px;
    background: var(--plum);
    display: flex; align-items: center; justify-content: flex-end;
    padding-right: 16px;
  }
  .company-name {
    color: var(--on-plum);
    font-weight: 400;
    font-size: 29px;
    line-height: 1;
  }
  .person {
    position: absolute; left: 456px; top: 92px;
  }
  .person-name {
    color: var(--plum);
    font-size: 29px; font-weight: 400; line-height: 1.1;
  }
  .person-title {
    font-size: 19px; font-weight: 400; margin-top: 4px;
  }
  .contact-details {
    position: absolute; top: 324px; left: 0; right: 0;
    font-size: 17px; line-height: 26px;
  }
  .detail-column { position: absolute; top: 0; font-style: normal; white-space: nowrap; }
  .street-address { right: 650px; text-align: right; }
  .postal-address { left: 352px; }
  .contact-numbers { left: 558px; }
  .column-rule {
    position: absolute; top: -10px; width: 2px; height: 114px;
    background: var(--plum);
  }
  .rule-one { left: 335px; }
  .rule-two { left: 541px; }
</style>
</head>
<body>
  <article class="business-card">
    <div class="accent-band"><span class="company-name">Kelmora Legal</span></div>

    <div class="person">
      <div class="person-name">Debra Lindqvist</div>
      <div class="person-title">Corporate Services Manager</div>
    </div>

    <div class="contact-details">
      <address class="detail-column street-address">
        Office 14 (Top Floor),<br>
        Toravel Business Centre,<br>
        Quinlan Grove Street, Alotau CBD,<br>
        Milne Bay Province.
      </address>
      <span class="column-rule rule-one"></span>
      <address class="detail-column postal-address">
        PO Box 593, Alotau, 211,<br>
        Milne Bay Province,<br>
        Papua New Guinea.
      </address>
      <span class="column-rule rule-two"></span>
      <div class="detail-column contact-numbers">
        T: +675 6418250<br>
        F: +675 6413362<br>
        M: +675 72915867<br>
        E: dlindqvist@kelmoraexample.com.pg.
      </div>
    </div>
  </article>
</body>
</html>
```